Bramble Bunnies Business Cards

I need a business card for my new Company called Bramble Bunnies. We create handmade baby moccasins, headbands, t-shirts and more. I want some that will appeal to parents, and to go with the colors of my logo that I have attached. feel free to be creative. I would like my logo placed somewhere on the card.

Industry/Entity Type

Retail

Contact Information for Business Card

Bramble Bunnies
20418 Wexley C #5127
Irvine Ca 92687
Rosalind Hatchett Ceo
Info@Bramble-Bunnies.com
www.Bramble-Bunnies.com
Phone 9495817302

Requirements
Nice to have
• Logo included

```html
<!DOCTYPE html>
<html lang="en">
<head>
<meta charset="utf-8">
<title>Bramble Bunnies Business Cards</title>
<link rel="stylesheet" href="https://fonts.googleapis.com/css2?family=Open+Sans:wght@300;400&display=swap">
<style>
  :root {
    --backdrop: #e9e6e1;
    --card: #fbfbfb;
    --card-shade: #ececec;
    --accent: #e8845a;
    --accent-soft: #f3d3c3;
    --ink: #3a3a3a;
    --ink-soft: #6b6b6b;
  }
  * { margin: 0; padding: 0; box-sizing: border-box; }
  html, body {
    width: 1200px;
    height: 600px;
    overflow: hidden;
    background: var(--backdrop);
    font-family: "Open Sans", sans-serif;
    color: var(--ink);
  }
  .card-sheet {
    position: relative;
    width: 1200px;
    height: 600px;
  }
  .card {
    position: absolute;
    top: 157px;
    width: 500px;
    height: 286px;
    background: linear-gradient(135deg, var(--card) 0%, var(--card) 55%, var(--card-shade) 100%);
    box-shadow: 0 6px 18px rgba(0,0,0,0.14);
  }
  .card--front { left: 60px; }
  .card--back { left: 640px; }

  /* Front */
  .brand {
    position: absolute;
    left: 46px;
    top: 52px;
    display: flex;
    align-items: center;
    gap: 14px;
  }
  .brand__mark {
    width: 26px;
    height: 26px;
    background: var(--accent);
  }
  .brand__name {
    font-size: 30px;
    font-weight: 300;
    color: var(--ink);
    letter-spacing: 0.2px;
  }
  .address {
    position: absolute;
    left: 48px;
    top: 122px;
    font-size: 13px;
    font-weight: 300;
    line-height: 19px;
    color: var(--ink-soft);
  }
  .contact-list {
    position: absolute;
    left: 48px;
    top: 183px;
    list-style: none;
    font-size: 13px;
    font-weight: 300;
    line-height: 19px;
    color: var(--ink-soft);
  }
  .contact-list li {
    display: flex;
    align-items: center;
    gap: 9px;
  }
  .contact-list svg { width: 10px; height: 10px; fill: var(--accent); }

  /* Back */
  .person {
    position: absolute;
    left: 46px;
    top: 60px;
  }
  .person__name {
    font-size: 17px;
    font-weight: 400;
    color: var(--accent);
  }
  .person__title {
    margin-top: 4px;
    padding-left: 128px;
    font-size: 13px;
    font-weight: 400;
    color: var(--ink);
  }
  .back-mark {
    position: absolute;
    right: 44px;
    top: 56px;
    width: 96px;
    height: 96px;
    border: 1px dashed #c9c9c9;
    padding: 8px;
  }
  .back-mark__fill {
    width: 100%;
    height: 100%;
    background: var(--accent-soft);
    opacity: 0.7;
  }
</style>
</head>
<body>
<main class="card-sheet">
  <section class="card card--front" aria-label="Business card front">
    <div class="brand">
      <span class="brand__mark"></span>
      <span class="brand__name">Bramble Bunnies</span>
    </div>
    <p class="address">20418 Wexley C #5127<br>Irvine Ca 92687</p>
    <ul class="contact-list">
      <li>
        <svg viewBox="0 0 10 10" aria-hidden="true"><rect x="1" y="0" width="8" height="10" rx="1.5"/></svg>
        9495817302
      </li>
      <li>
        <svg viewBox="0 0 10 10" aria-hidden="true"><path d="M0 2h10v6H0z M0 2l5 3.5L10 2" /></svg>
        Info@Bramble-Bunnies.com
      </li>
      <li>
        <svg viewBox="0 0 10 10" aria-hidden="true"><circle cx="5" cy="5" r="5"/></svg>
        www.Bramble-Bunnies.com
      </li>
    </ul>
  </section>

  <section class="card card--back" aria-label="Business card back">
    <div class="person">
      <p class="person__name">Rosalind Hatchett</p>
      <p class="person__title">Ceo</p>
    </div>
    <div class="back-mark"><div class="back-mark__fill"></div></div>
  </section>
</main>
</body>
</html>
```